Buisness card

**Front Side:**

**[Your Company Logo]**
**Steadfast Upkeep Engineering**
*Keeping Your Equipment Running Smoothly*

**Contact Information:**
- **Name:** [dale Harwick
- **Title:** [owner
- **Phone:** [5073918246
- **Email:** dale@suevx.com

**Back Side:**

**Services Offered:**
- Routine Inspections
- Equipment Maintenance
- Emergency Repairs
- Consultation Services
- New installs
Tag line
Be proactive not reactive

```html
<!DOCTYPE html>
<html lang="en">
<head>
<meta charset="utf-8">
<title>Steadfast Upkeep Engineering — Business Card</title>
<link href="https://fonts.googleapis.com/css2?family=Montserrat:wght@500;600;700;800&display=swap" rel="stylesheet">
<style>
  :root {
    --stage: #2a2a2c;
    --paper: #ffffff;
    --navy: #0b2a6e;
    --bright: #0a74f5;
    --accent: #1f7cf0;
    --ink-blue: #0b3d9c;
    --white: #ffffff;
  }
  * { box-sizing: border-box; margin: 0; padding: 0; }
  html, body { width: 1200px; height: 875px; overflow: hidden; }
  body {
    background: var(--stage);
    font-family: "Montserrat", sans-serif;
    position: relative;
  }
  .card {
    position: absolute;
    top: 277px;
    width: 540px;
    height: 320px;
    border-radius: 18px;
    background: var(--paper);
    overflow: hidden;
  }
  .card--back { left: 40px; }
  .card--front { left: 620px; }
  .card__wave { position: absolute; inset: 0; width: 100%; height: 100%; }

  .brand {
    position: absolute;
    top: 44px;
    left: 34px;
    display: flex;
    align-items: center;
    gap: 16px;
  }
  .brand__mark {
    width: 66px; height: 66px;
    border-radius: 50%;
    background: var(--navy);
    flex: none;
  }
  .brand__name {
    font-weight: 800;
    font-size: 21px;
    line-height: 1.1;
    color: var(--ink-blue);
    text-transform: uppercase;
    letter-spacing: 0.5px;
    width: 330px;
  }
  .brand__tagline {
    margin-top: 8px;
    display: flex;
    align-items: center;
    gap: 8px;
    font-weight: 700;
    font-size: 11px;
    color: var(--navy);
    text-transform: uppercase;
    letter-spacing: 0.6px;
    white-space: nowrap;
  }
  .brand__tagline::before,
  .brand__tagline::after {
    content: "";
    width: 22px; height: 2px;
    background: var(--accent);
  }
  .card--front .brand__tagline { font-size: 10px; letter-spacing: 0.4px; }
  .card--front .brand__tagline::before,
  .card--front .brand__tagline::after { width: 16px; }

  .services {
    position: absolute;
    left: 30px; right: 30px;
    top: 224px;
    color: var(--white);
    text-align: center;
  }
  .services__title {
    font-weight: 800;
    font-size: 20px;
    letter-spacing: 0.6px;
    text-transform: uppercase;
    margin-bottom: 8px;
  }
  .services__list {
    font-weight: 600;
    font-size: 11px;
    line-height: 1.7;
    text-transform: uppercase;
    letter-spacing: 0.4px;
  }
  .services__dot { color: #3d94ff; margin: 0 5px; }

  .person {
    position: absolute;
    left: 40px;
    top: 250px;
    color: var(--white);
    text-align: right;
  }
  .person__name {
    font-weight: 800;
    font-size: 24px;
    letter-spacing: 0.6px;
    text-transform: uppercase;
  }
  .person__title { font-weight: 500; font-size: 12px; }
  .divider {
    position: absolute;
    left: 300px; top: 190px;
    width: 1.5px; height: 80px;
    background: rgba(255,255,255,0.85);
  }
  .contacts {
    position: absolute;
    left: 318px; top: 192px;
    list-style: none;
    color: var(--white);
    font-weight: 500;
    font-size: 13px;
  }
  .contacts li { display: flex; align-items: center; gap: 9px; margin-bottom: 9px; }
  .contacts svg { width: 14px; height: 14px; flex: none; }
</style>
</head>
<body>

  <section class="card card--back" aria-label="Business card back">
    <svg class="card__wave" viewBox="0 0 540 320" preserveAspectRatio="none" aria-hidden="true">
      <path d="M0 205 C120 180 180 240 300 182 S450 82 540 86" fill="none" stroke="var(--accent)" stroke-width="3"/>
      <path d="M0 215 C120 190 180 250 300 192 S450 92 540 96 L540 320 L0 320Z" fill="var(--navy)"/>
    </svg>
    <div class="brand">
      <span class="brand__mark"></span>
      <div>
        <div class="brand__name">Steadfast Upkeep Engineering</div>
        <div class="brand__tagline">Be proactive not reactive</div>
      </div>
    </div>
    <div class="services">
      <h2 class="services__title">Services Offered:</h2>
      <p class="services__list">
        Routine Inspections<span class="services__dot">•</span>Equipment Maintenance<span class="services__dot">•</span>New Installs<br>
        Emergency Repairs<span class="services__dot">•</span>Consultation Services
      </p>
    </div>
  </section>

  <section class="card card--front" aria-label="Business card front">
    <svg class="card__wave" viewBox="0 0 540 320" preserveAspectRatio="none" aria-hidden="true">
      <path d="M0 245 C110 240 170 205 270 178 S430 128 540 124" fill="none" stroke="var(--navy)" stroke-width="3"/>
      <path d="M0 255 C110 250 170 215 270 188 S430 138 540 134 L540 320 L0 320Z" fill="var(--bright)"/>
    </svg>
    <div class="brand">
      <span class="brand__mark"></span>
      <div>
        <div class="brand__name">Steadfast Upkeep Engineering</div>
        <div class="brand__tagline">Keeping your equipment running smoothly</div>
      </div>
    </div>
    <div class="person">
      <div class="person__name">Dale Harwick</div>
      <div class="person__title">Owner</div>
    </div>
    <span class="divider"></span>
    <ul class="contacts">
      <li>
        <svg viewBox="0 0 24 24" aria-hidden="true"><path fill="#fff" d="M6.6 10.8a15.1 15.1 0 0 0 6.6 6.6l2.2-2.2c.3-.3.7-.4 1-.2 1.1.4 2.3.6 3.6.6.6 0 1 .4 1 1V20c0 .6-.4 1-1 1A17 17 0 0 1 3 4c0-.6.4-1 1-1h3.5c.6 0 1 .4 1 1 0 1.3.2 2.5.6 3.6.1.3 0 .7-.2 1z"/></svg>
        5073918246
      </li>
      <li>
        <svg viewBox="0 0 24 24" aria-hidden="true"><path fill="#fff" d="M3 5h18v14H3z"/><path d="M3 5l9 8 9-8" fill="none" stroke="var(--bright)" stroke-width="2"/></svg>
        dale@suevx.com
      </li>
      <li>
        <svg viewBox="0 0 24 24" aria-hidden="true"><circle cx="12" cy="12" r="9" fill="none" stroke="#fff" stroke-width="2"/><path d="M3 12h18M12 3c3 3 3 15 0 18M12 3c-3 3-3 15 0 18" fill="none" stroke="#fff" stroke-width="1.6"/></svg>
        suevx.com
      </li>
    </ul>
  </section>

</body>
</html>
```